Renata Quisby

Luxury And Style -

Black - White & Gold

Target Market(s)

Fashion

Industry/Entity Type

Fashion

Requirements
Must have
• High-End
Nice to have
• We will Print on Silk Paper

```html
<!DOCTYPE html>
<html lang="en">
<head>
<meta charset="utf-8">
<title>Renata Quisby — Letterhead</title>
<link rel="stylesheet" href="https://fonts.googleapis.com/css2?family=Poppins:wght@400;500&family=Open+Sans:wght@400&display=swap">
<style>
  :root {
    --ink-navy: #0e121c;
    --gold: #e0a640;
    --gold-soft: #f0c987;
    --gold-pale: #f8e6c4;
    --text-dark: #2b2b2b;
    --text-body: #5a5a5a;
    --paper: #ffffff;
  }
  * { margin: 0; padding: 0; box-sizing: border-box; }
  html, body { width: 922px; height: 1200px; overflow: hidden; background: var(--paper); }
  .letterhead { position: relative; width: 922px; height: 1200px; background: var(--paper); font-family: "Poppins", sans-serif; color: var(--text-body); }

  .masthead { position: absolute; left: 0; top: 0; width: 100%; height: 146px; background: var(--ink-navy); display: flex; flex-direction: column; align-items: center; justify-content: center; gap: 6px; }
  .brand-name { font-weight: 500; font-size: 24px; letter-spacing: 4px; color: var(--gold); text-transform: uppercase; }
  .brand-tagline { font-weight: 500; font-size: 10px; letter-spacing: 1.5px; color: var(--gold); text-transform: uppercase; }

  .lace-band { position: absolute; left: 0; top: 151px; width: 100%; height: 30px; background: linear-gradient(180deg, var(--gold-soft), var(--gold-pale)); }

  .sender { position: absolute; left: 83px; top: 290px; }
  .sender-name { font-weight: 500; font-size: 26px; color: var(--text-dark); line-height: 1.2; }
  .sender-role { font-family: "Open Sans", sans-serif; font-size: 12px; color: var(--text-body); margin-top: 2px; }

  .contact-list { position: absolute; left: 83px; top: 347px; list-style: none; font-family: "Open Sans", sans-serif; font-size: 14px; color: var(--text-dark); }
  .contact-list li { height: 25px; line-height: 25px; }
  .contact-key { display: inline-block; width: 24px; color: var(--gold); }

  .letter-date { position: absolute; right: 82px; top: 414px; font-family: "Open Sans", sans-serif; font-size: 17px; color: var(--text-dark); }

  .letter-body { position: absolute; left: 83px; top: 481px; width: 758px; font-size: 14.6px; line-height: 25.5px; text-align: justify; }
  .letter-body p + p { margin-top: 25px; }

  .signature-mark { position: absolute; left: 690px; top: 866px; width: 130px; height: 76px; background: linear-gradient(135deg, #f1f1f1, #e2e2e2); border-radius: 4px; }
  .signatory { position: absolute; right: 99px; top: 950px; font-weight: 500; font-size: 16px; color: var(--text-dark); }

  .footer-contacts { position: absolute; left: 83px; top: 988px; list-style: none; font-family: "Open Sans", sans-serif; font-size: 12px; color: var(--text-body); line-height: 15px; }
  .footer-contacts li { display: flex; align-items: flex-start; gap: 7px; margin-bottom: 14px; }
  .footer-contacts li:first-child { margin-bottom: 17px; }
  .icon-box { width: 16px; height: 16px; flex: none; background: var(--ink-navy); border-radius: 2px; display: flex; align-items: center; justify-content: center; }

  .corner-ornament { position: absolute; top: 1092px; width: 332px; height: 76px; }
  .corner-ornament.left { left: 30px; }
  .corner-ornament.right { right: 30px; }
  .ornament-post { position: absolute; top: 0; width: 14px; height: 62px; background: linear-gradient(180deg, var(--gold-soft), var(--gold-pale)); }
  .ornament-rail { position: absolute; bottom: 0; left: 0; width: 100%; height: 16px; background: linear-gradient(90deg, var(--gold-soft), var(--gold-pale)); }
  .corner-ornament.left .ornament-post { left: 0; }
  .corner-ornament.right .ornament-post { right: 0; }
  .corner-ornament.right .ornament-rail { background: linear-gradient(90deg, var(--gold-pale), var(--gold-soft)); }
</style>
</head>
<body>
<main class="letterhead">
  <header class="masthead">
    <div class="brand-name">Renata Quisby</div>
    <div class="brand-tagline">Luxury and Style</div>
  </header>
  <div class="lace-band" role="img" aria-label="Gold lace ornament border"></div>

  <section class="sender">
    <h1 class="sender-name">Alden Marsh</h1>
    <div class="sender-role">Chief Director</div>
  </section>

  <ul class="contact-list">
    <li><span class="contact-key">A :</span>218 Linden Row, Fairhaven, FH 40112</li>
    <li><span class="contact-key">W :</span>www.renataquisby.com</li>
    <li><span class="contact-key">P :</span>+00 555 019 42</li>
    <li><span class="contact-key">M :</span>hello@renataquisby.com</li>
  </ul>
  <div class="letter-date">12 December, 2025</div>

  <article class="letter-body">
    <p>Lorem ipsum dolor sit amet, consectetuer adipiscing elit, sed diam nonummy nibh euismod tincidunt ut laoreet dolore magna aliquam erat volutpat. Ut wisi enim ad minim veniam, quis nostrud exerci tation ullamcorper suscipit lobortis nisl ut aliquip ex ea commodo consequat. Duis autem vel eum iriure dolor in hendrerit in vulputate velit esse molestie consequat, vel illum dolore eu feugiat nulla facilisis at vero eros et accumsan et iusto odio dignissim qui blandit praesent luptatum zzril delenit augue duis dolore te feugait nulla facilisi.</p>
    <p>Lorem ipsum dolor sit amet, cons ectetuer adipiscing elit, sed diam nonummy nibh euismod tincidunt ut laoreet dolore magna aliquam erat volutpat. Ut wisi enim ad minim veniam, quis nostrud exerci tation ullamcorper suscipit lobortis nisl ut aliquip ex ea commodo consequat. Lorem ipsum dolor sit amet, consectetuer adipiscing elit, sed diam nonummy nibh euismod tincidunt ut laoreet dolore magna aliquam eratveniam. suscipit lobortis nisl ut aliquip ex ea commodo consequat. Lorem ipsum dolor sit amet, consectetuer adipiscing elit, sed diam nonummy nibh euismod tincidunt ut laoreet dolore magna aliquam eratveniam.</p>
  </article>

  <div class="signature-mark" role="img" aria-label="Handwritten signature"></div>
  <div class="signatory">Mr. Alden Marsh</div>

  <ul class="footer-contacts">
    <li><span class="icon-box"><svg width="10" height="10" viewBox="0 0 10 10"><path d="M5 0.5a3.2 3.2 0 0 0-3.2 3.2C1.8 6 5 9.5 5 9.5s3.2-3.5 3.2-5.8A3.2 3.2 0 0 0 5 0.5z" fill="#fff"/><circle cx="5" cy="3.7" r="1.2" fill="#0e121c"/></svg></span><span>218 Linden Row<br>Fairhaven, FH 40112</span></li>
    <li><span class="icon-box"><svg width="10" height="10" viewBox="0 0 10 10"><path d="M2.2 0.8l1.6 2-0.9 1.1c0.6 1.2 1.5 2.1 2.7 2.7l1.1-0.9 2 1.6-0.8 1.6C4.8 8.7 1.3 5.2 0.6 1.6z" fill="#fff"/></svg></span><span>+00 555 019 42</span></li>
    <li><span class="icon-box"><svg width="10" height="10" viewBox="0 0 10 10"><rect x="0.8" y="2" width="8.4" height="6" fill="#fff"/><path d="M0.8 2l4.2 3.3L9.2 2" stroke="#0e121c" stroke-width="0.9" fill="none"/></svg></span><span>hello@renataquisby.com</span></li>
    <li><span class="icon-box"><svg width="10" height="10" viewBox="0 0 10 10"><path d="M2 1l6 3.6-2.6 0.6 1.6 2.8-1.1 0.6-1.6-2.8L2.5 7.5z" fill="#fff"/></svg></span><span>www.renataquisby.com</span></li>
  </ul>

  <div class="corner-ornament left" role="img" aria-label="Gold corner ornament flourish">
    <div class="ornament-post"></div>
    <div class="ornament-rail"></div>
  </div>
  <div class="corner-ornament right" role="img" aria-label="Gold corner ornament flourish">
    <div class="ornament-post"></div>
    <div class="ornament-rail"></div>
  </div>
</main>
</body>
</html>
```